Plumbing Trifold Design for Restoration Company

We would like this brochure to match our current KVT branding and marketing materials. The overall look should feel modern, clean, premium, and trustworthy.

Our brand colors are included in the attached files along with a picture of what our current marketing material looks like. We'd like to use real KVT photography whenever possible rather than stock images, but if stock images are necessary, please go ahead and use.

The brochure should communicate that KVT is a full-service plumbing company backed by years of experience in both traditional plumbing and complex pipe restoration.

Front Page: we would like to include logo, phone number (800-318-4957), website (www.kvtflow.example) and then maybe the following: "Traditional Plumbing Services", "residential & commercial, 24/7 Emergency Service, Licensed & Insured" and can also add "reliable Repairs. Honest Service. Lasting Solutions" if spacing allows.

Other sections we would like included (not in any particular order):

-Why Choose KVT?:
Family-oriented team
Licensed & insured professionals
Residential & commercial expertise
Honest recommendations
Quality workmanship
Emergency service available
Clean, respectful technicians
One trusted company for plumbing and sewer solutions
____________________________
Our Story:
Built on solving complex plumbing challenges. Trusted for every plumbing need.
Since our founding, Conduit Renewal Partners has built a reputation for helping homeowners, businesses, and property managers solve some of the industry’s most challenging plumbing and sewer problems through quality workmanship, professionalism, and innovative solutions.
As our customers’ needs have grown, so has our commitment to serving them. What began as a leader in pipe restoration has expanded into full-service plumbing, allowing us to provide complete plumbing solutions—from everyday repairs and fixture replacements to water heaters, drain cleaning, repiping, and emergency plumbing services.
Today, our traditional plumbing division delivers the same level of expertise, communication, and customer care that KVT has become known for. Whether it’s a simple repair or a complex plumbing project, our goal remains the same: to provide dependable solutions, lasting quality, and an exceptional customer experience every step of the way.
-Our Values:
The KVT Way
Professional - Don't settle for good, BE GREAT
Responsive - When there's a need, BE FIRST!
Service - Life is not about you, BE ABOUT OTHERS!
These three values guide everything we do
Complete Plumbing Solutions:
-Plumbing Repairs
Reliable solutions to keep your plumbing system running safely and efficiently.
Leak detection & repair
Pipe Burst Repairs
Water line repairs
Whole-home repiping

-Fixtures & Installations
Professional installation, repair, and replacement of the fixtures you use every day.
Faucets
Toilets
Sinks
Showers & tubs
Garbage disposals
Hose bibs
Shut-off valves

-Water Heater Services
Whether you need a repair, replacement, or routine maintenance, we'll keep your hot water flowing.
Water heater repair
Water heater replacement
Tankless water heaters
Expansion tanks
Recirculation pumps
Preventative maintenance

-Drain & Sewer Solutions
From routine drain cleaning to complete sewer repairs, our team has the equipment and expertise to get your plumbing flowing again.
Drain cleaning
Hydro jetting
Camera inspections
Main sewer line cleaning
Sewer line repair
Sewer line replacement
Emergency drain backups
maybe add in a blurb saying
"Need a Trenchless Solution?
Ask about our non-invasive solutions as an alternative to traditional replacement for sewer and storm drain systems"
Testimonials:
"This company is fantastic, very professional and knowledgeable. Use them at several of my communities I manage and highly recommend them!" Belvine Townhomes
"KVT continues to be the primary plumbing vendor I use for all of my properties throughout Tampa Bay!" Corliss Dunes Condominium
"KVT did a great job at a great price and have always been willing to help with their abundance of knowledge prior to even working on projects for our community!" Townhomes at Hollow Fern
"KVT is amazing! My office flooded out on a Friday night and they responded within a couple hours to make the needed repair. The team was professional and got right to work (there van was also immaculate, which tells you a lot about hot they operate). Would definitely recommend them to anyone!" Dorin Welsby
______________________
Ready to get started?
Whether it's a leaking pipe, a new water heater, a clogged drain, or a plumbing emergency, our team is here to help
800-318-4957
info@kvtflow.example
www.kvtflow.example

Additional Information: please feel free to edit any of the pictures provided and AI files can be provided for the other marketing material if helpful. We would like an AI file and PDF ready print if possible.
Thank you!

commercial and residential property owners

Plumbing

Colors
0054AA
0677BA
7BADD7
CADEEF
E8F1F8

Must have
• My project must flow with current marketing material colors
Nice to have
• would like the front page picture to fade nicely into background

```html
<!DOCTYPE html>
<html lang="en">
<head>
<meta charset="utf-8">
<title>KVT Trifold Brochure</title>
<link rel="stylesheet" href="https://fonts.googleapis.com/css2?family=Russo+One&family=Roboto:wght@400;500;700&display=swap">
<style>
:root{
  --navy:#1a1e2c;
  --navy-2:#232939;
  --brand-deep:#0054AA;
  --brand:#0677BA;
  --brand-bright:#1f8ee0;
  --brand-soft:#7BADD7;
  --brand-pale:#CADEEF;
  --brand-mist:#E8F1F8;
  --white:#ffffff;
  --ink:#1b1d24;
  --stage:#9b9b9b;
  --head:"Russo One",sans-serif;
  --body:"Roboto",sans-serif;
}
*{box-sizing:border-box;margin:0;padding:0}
html,body{width:1200px;height:3423px;overflow:hidden}
body{background:var(--stage);font-family:var(--body);color:var(--white);position:relative}
.sheet{position:absolute;left:49px;width:1102px;height:779px;overflow:hidden}
.sheet-outer{top:902px}
.sheet-inner{top:1741px}
.spread{position:absolute;left:0;top:0;width:828px;height:585px;transform:scale(1.331);transform-origin:0 0;background:var(--navy);overflow:hidden}
.abs{position:absolute}
.frame-lines{position:absolute;left:0;top:0;width:828px;height:585px;pointer-events:none}
.photo{position:absolute}
/* headings */
.h-head{font-family:var(--head);font-weight:400;line-height:1}
.blue{color:var(--brand-bright)}
/* outer: left panel */
.emergency-badge{left:39px;top:24px;width:56px;height:64px;border:2px solid var(--brand-bright);color:var(--brand-bright);text-align:center;font-family:var(--head);padding-top:4px}
.emergency-badge .big{font-size:22px;display:block;line-height:1}
.emergency-badge .small{font-size:7px;display:block;line-height:1.1;margin-top:2px}
.trenchless{left:109px;top:18px;font-size:21px;line-height:1.13}
.trenchless-note{left:109px;top:104px;width:155px;font-size:7.4px;line-height:1.45}
.social-label{left:36px;top:106px;font-size:8.5px}
.social-dots{left:36px;top:122px;display:flex;gap:11px}
.social-dots span{width:12px;height:12px;border-radius:50%;background:var(--brand)}
.why-panel{left:0;top:170px;width:254px;height:415px;background:var(--white)}
.why-title{left:24px;top:196px;font-size:18px;color:var(--brand-deep)}
.why-list{left:24px;top:224px;width:215px;list-style:none;color:var(--ink);font-size:10.6px;font-weight:500}
.why-list li{height:27.5px;display:flex;align-items:center;border-bottom:1px solid #e3e6ea;padding-left:18px;position:relative}
.why-list li::before{content:"";position:absolute;left:2px;top:9px;border-left:8px solid var(--brand-deep);border-top:5px solid transparent;border-bottom:5px solid transparent}
.why-close{left:24px;top:426px;width:210px;color:var(--ink);font-size:10.6px;line-height:1.3}
.van-photo{left:8px;top:466px;width:240px;height:116px;background:linear-gradient(180deg,#f6f7f9 0%,#e4e8ee 60%,#c9ced6 100%)}
/* middle */
.ready{left:276px;width:276px;text-align:center}
.ready-top{top:22px;font-size:22px}
.ready-bottom{top:52px;font-size:22px;color:var(--brand-bright)}
.ready-copy{top:88px;font-size:8.4px;line-height:1.4;padding:0 40px}
.testi-title{top:152px;font-size:20px;color:var(--brand-bright)}
.testimonial{left:309px;width:212px;background:var(--navy-2);border:1px solid #2c3346;border-radius:3px;text-align:center;padding:10px 12px 0;font-size:7.6px;line-height:1.45;color:#e3e7ee}
.testimonial cite{display:block;margin-top:6px;font-style:normal;font-weight:700;color:var(--brand-bright);font-size:9px}
.t1{top:187px;height:84px}
.t2{top:283px;height:83px}
.t3{top:378px;height:89px}
.contact-band{left:276px;top:480px;width:276px;height:105px;background:linear-gradient(90deg,#0a3f8e,var(--brand) 70%,var(--brand-bright))}
.contact-list{left:340px;top:520px;list-style:none;font-size:12.5px;font-weight:500;line-height:1.32}
.contact-list li{display:flex;align-items:center;gap:6px}
.contact-list svg{width:10px;height:10px}
/* right cover */
.brand-mark{display:flex;align-items:center;gap:8px;font-family:var(--head);color:var(--white)}
.brand-mark .sq{width:20px;height:20px;background:var(--brand-bright)}
.brand-mark .name{font-size:40px;line-height:1;letter-spacing:3px}
.brand-sub{font-family:var(--head);font-size:7.5px;letter-spacing:2.2px;color:var(--white)}
.cover-logo{left:599px;top:22px}
.cover-sub{left:599px;top:66px}
.cover-box{left:562px;top:92px;width:262px;height:320px;border-radius:10px;background:linear-gradient(135deg,#0b3f92,var(--brand) 60%,var(--brand-bright));border:3px solid #0a3c8c}
.cover-eyebrow{left:562px;top:112px;width:262px;display:flex;align-items:center;justify-content:center;gap:7px;font-size:15px;letter-spacing:1px}
.cover-eyebrow i{display:block;width:22px;height:1.5px;background:var(--white)}
.cover-title{left:588px;top:134px;font-size:30px;line-height:1}
.cover-photo{left:572px;top:205px;width:252px;height:198px;background:linear-gradient(160deg,#d9dde2 0%,#9aa3ad 45%,#3b4350 100%);border-radius:0 0 8px 8px}
.features{left:562px;top:420px;width:262px;display:flex}
.feature{flex:1;text-align:center;font-size:7.6px;line-height:1.25;border-right:1px solid #39405a;padding-top:2px}
.feature:last-child{border-right:0}
.feature svg{width:22px;height:22px;display:block;margin:0 auto 4px}
.phone-big{font-family:var(--head);font-size:25px;letter-spacing:.5px}
.web-spaced{font-size:10.5px;letter-spacing:5.2px;color:var(--brand-bright)}
.tagline{font-size:6.3px;color:#c8d0dc;letter-spacing:.4px}
.cover-foot{left:552px;top:512px;width:276px;text-align:center}
/* inner left */
.values-panel{left:0;top:0;width:258px;height:232px;background:var(--white);color:var(--ink)}
.values-title{left:0;top:20px;width:258px;text-align:center;font-size:22px;color:var(--brand-deep)}
.values-sub{left:0;top:50px;width:258px;text-align:center;font-size:7.8px;font-weight:500;color:var(--ink)}
.value-ring{width:54px;height:54px;border-radius:50%;background:var(--brand-mist);border:4px solid #e3e7ec;display:flex;align-items:center;justify-content:center}
.value-ring span{width:40px;height:40px;border-radius:50%;background:var(--brand-deep);display:flex;align-items:center;justify-content:center}
.value-ring svg{width:22px;height:22px}
.values-row{left:14px;top:70px;width:230px;display:flex;justify-content:space-between}
.values-labels{left:14px;top:138px;width:230px;display:flex;justify-content:space-between;color:var(--ink);text-align:center;font-size:7.8px;line-height:1.2}
.values-labels div{width:72px}
.values-labels b{display:block;font-size:8.2px}
.values-close{left:0;top:196px;width:258px;text-align:center;color:var(--ink);font-size:8.6px}
.story-title{left:24px;top:258px;font-size:22px;color:var(--brand-bright)}
.story-copy{left:24px;top:296px;width:205px;font-size:7.6px;line-height:1.5;color:#dfe4ec}
.story-copy p+p{margin-top:12px}
.story-foot{left:24px;top:545px}
/* services */
.services-box{left:269px;top:20px;width:545px;height:480px;background:var(--white);border:4px solid var(--brand-deep);border-radius:10px}
.services-title{left:301px;top:50px;font-size:28px;color:var(--ink)}
.svc{position:absolute;color:var(--ink);width:240px}
.svc h3{font-family:var(--head);font-weight:400;color:var(--brand-deep);font-size:13px;display:flex;align-items:center;gap:7px;margin-bottom:6px}
.svc h3 svg{width:17px;height:17px}
.svc p{font-size:8.6px;line-height:1.35;margin-bottom:8px}
.svc ul{list-style:none;font-size:8.6px;line-height:1.6;text-transform:uppercase}
.svc li{padding-left:12px;position:relative}
.svc li::before{content:"";position:absolute;left:0;top:3.5px;border-left:5px solid var(--brand);border-top:3.5px solid transparent;border-bottom:3.5px solid transparent}
.svc .cols{display:flex;gap:38px}
.svc-repairs{left:301px;top:113px}
.svc-fixtures{left:301px;top:255px}
.svc-heater{left:577px;top:113px;width:215px}
.svc-drain{left:577px;top:285px;width:215px}
.services-logo{left:301px;top:416px}
.services-logo .name{font-size:36px;color:var(--ink)}
.services-logo .sq{background:var(--brand-deep)}
.services-logo-sub{left:301px;top:457px;color:var(--ink);font-size:8px}
.heater-photo{left:276px;top:505px;width:276px;height:80px;background:linear-gradient(90deg,#3a3f49,#7a8590 45%,#2b303a)}
.inner-foot{left:552px;top:512px;width:276px;text-align:center}
</style>
</head>
<body>

<!-- Outer spread -->
<section class="sheet sheet-outer">
  <div class="spread">
    <div class="abs why-panel"></div>

    <svg class="frame-lines" viewBox="0 0 828 585" fill="none">
      <path d="M6 0 V148 Q6 160 18 160 H250 Q262 160 262 172 V585" stroke="#ffffff" stroke-width="4"/>
      <path d="M268 585 V178 Q268 154 244 154" stroke="#0a4fa3" stroke-width="5"/>
      <path d="M552 98 V410 Q552 432 574 432 H810 Q822 432 822 420 V0" stroke="#0a4fa3" stroke-width="5"/>
      <path d="M806 10 V30" stroke="#ffffff" stroke-width="6"/>
      <path d="M780 410 H806 Q818 410 818 422 V440" stroke="#ffffff" stroke-width="6"/>
      <path d="M562 188 V230" stroke="#ffffff" stroke-width="6"/>
      <path d="M262 395 V435" stroke="#ffffff" stroke-width="6"/>
    </svg>

    <div class="abs emergency-badge"><span class="big">24/7</span><span class="small">EMERGENCY<br>SERVICE</span></div>
    <div class="abs trenchless h-head">Need a<br><span class="blue">Trenchless<br>Solution?</span></div>
    <div class="abs social-label">Social Media</div>
    <div class="abs social-dots" aria-label="Social media links"><span></span><span></span><span></span></div>
    <p class="abs trenchless-note">Ask about our non-invasive solutions as an alternative to traditional replacement for sewer and storm drain systems</p>

    <h2 class="abs why-title h-head">Why Choose KVT?</h2>
    <ul class="abs why-list">
      <li>Family-oriented team</li>
      <li>Licensed &amp; insured professionals</li>
      <li>Residential &amp; commercial expertise</li>
      <li>Honest recommendations</li>
      <li>Quality workmanship</li>
      <li>Emergency service available</li>
      <li>Clean, respectful technicians</li>
    </ul>
    <p class="abs why-close">One trusted company for plumbing and sewer solutions</p>
    <div class="photo van-photo" role="img" aria-label="Photo of a white KVT service van"></div>

    <h2 class="abs ready ready-top h-head">READY TO</h2>
    <h2 class="abs ready ready-bottom h-head">GET STARTED?</h2>
    <p class="abs ready ready-copy">Whether it's a leaking pipe, a new water heater, a clogged drain, or a plumbing emergency, our team is here to help</p>
    <h2 class="abs ready testi-title h-head">Testimonials</h2>
    <blockquote class="abs testimonial t1">"This company is fantastic, very professional and knowledgeable. Use them at several of my communities I manage and highly recommend them!"<cite>Belvine Townhomes</cite></blockquote>
    <blockquote class="abs testimonial t2">"KVT continues to be the primary plumbing vendor I use for all of my properties throughout Tampa Bay!"<cite>Corliss Dunes Condominium</cite></blockquote>
    <blockquote class="abs testimonial t3">"KVT did a great job at a great price and have always been willing to help with their abundance of knowledge prior to even working on projects for our community!"<cite>Townhomes at Hollow Fern</cite></blockquote>

    <div class="abs contact-band"></div>
    <ul class="abs contact-list">
      <li><svg viewBox="0 0 10 10"><circle cx="5" cy="5" r="5" fill="#fff"/><path d="M3 2.5 4 4 3.6 4.6Q4.5 6 5.4 6.4L6 6 7.5 7 7 7.8Q4.5 7.8 2.2 3.2Z" fill="#0677BA"/></svg>800-318-4957</li>
      <li><svg viewBox="0 0 10 10"><circle cx="5" cy="5" r="5" fill="#fff"/><rect x="2.4" y="3.2" width="5.2" height="3.6" fill="none" stroke="#0677BA" stroke-width=".8"/><path d="M2.4 3.2 5 5.3 7.6 3.2" fill="none" stroke="#0677BA" stroke-width=".8"/></svg>info@kvtflow.example</li>
      <li><svg viewBox="0 0 10 10"><circle cx="5" cy="5" r="5" fill="#fff"/><circle cx="5" cy="5" r="2.8" fill="none" stroke="#0677BA" stroke-width=".7"/><path d="M2.2 5H7.8M5 2.2V7.8" stroke="#0677BA" stroke-width=".6"/></svg>www.kvtflow.example</li>
    </ul>

    <div class="abs cover-logo brand-mark"><span class="sq"></span><span class="name">KVT</span></div>
    <div class="abs cover-sub brand-sub">CONDUIT RENEWAL PARTNERS</div>
    <div class="abs cover-box"></div>
    <div class="abs cover-eyebrow"><i></i>TRADITIONAL<i></i></div>
    <h1 class="abs cover-title h-head">PLUMBING<br>SERVICES</h1>
    <div class="photo cover-photo" role="img" aria-label="Photo of a KVT plumber working on pipes under a sink, fading into the background"></div>

    <div class="abs features">
      <div class="feature"><svg viewBox="0 0 22 22" fill="none" stroke="#fff" stroke-width="1.4"><rect x="4" y="5" width="14" height="14"/><path d="M2 5H20M7 9h2M13 9h2M7 13h2M13 13h2M10 19v-3h2v3"/></svg>Residential &amp;<br>commercial<br>Services</div>
      <div class="feature"><svg viewBox="0 0 22 22" fill="none" stroke="#fff" stroke-width="1.4"><path d="M19 11A8 8 0 1 1 11 3"/><path d="M11 7V11L14 13"/><path d="M15 2 19 3 18 7"/></svg>24/7<br>Emergency<br>Service</div>
      <div class="feature"><svg viewBox="0 0 22 22" fill="none" stroke="#fff" stroke-width="1.4"><path d="M5 2H14L18 6V20H5Z"/><path d="M8 8H15M8 11H15M8 14H12"/><circle cx="15" cy="16" r="2.5"/></svg>Licensed<br>&amp; Insured<br>Services</div>
    </div>

    <div class="abs cover-foot">
      <div class="phone-big">800-318-4957</div>
      <div class="web-spaced">WWW.KVTFLOW.EXAMPLE</div>
      <div class="tagline">Reliable Repairs | Honest Service | Lasting Solutions</div>
    </div>
  </div>
</section>

<!-- Inner spread -->
<section class="sheet sheet-inner">
  <div class="spread">
    <div class="abs values-panel"></div>
    <div class="abs services-box"></div>

    <svg class="frame-lines" viewBox="0 0 828 585" fill="none">
      <path d="M10 0 V226 Q10 232 18 232 H254 Q266 232 266 244 V585" stroke="#0a4fa3" stroke-width="5"/>
      <path d="M6 0 V222 Q6 228 14 228 H250" stroke="#ffffff" stroke-width="2"/>
      <path d="M289 8 V0" stroke="#ffffff" stroke-width="6"/>
      <path d="M4 212 V230" stroke="#ffffff" stroke-width="6"/>
      <path d="M812 200 V240" stroke="#ffffff" stroke-width="6"/>
    </svg>

    <h2 class="abs values-title h-head">Our Values</h2>
    <div class="abs values-sub">THE KVT WAY</div>
    <div class="abs values-row">
      <div class="value-ring"><span><svg viewBox="0 0 22 22" fill="none" stroke="#fff" stroke-width="1.4"><circle cx="11" cy="7" r="2.6"/><circle cx="5" cy="9" r="2"/><circle cx="17" cy="9" r="2"/><path d="M6 18Q6 12 11 12Q16 12 16 18M1.5 16Q2 12.5 5 12.5M20.5 16Q20 12.5 17 12.5"/></svg></span></div>
      <div class="value-ring"><span><svg viewBox="0 0 22 22" fill="none" stroke="#fff" stroke-width="1.4"><rect x="3" y="4" width="16" height="11" rx="1"/><path d="M8 19H14M11 15V19"/></svg></span></div>
      <div class="value-ring"><span><svg viewBox="0 0 22 22" fill="none" stroke="#fff" stroke-width="1.4"><circle cx="11" cy="11" r="3"/><circle cx="11" cy="11" r="7" stroke-dasharray="3 2"/></svg></span></div>
    </div>
    <div class="abs values-labels">
      <div><b>Professional</b>Don't settle for good, BE GREAT</div>
      <div><b>Responsive</b>When there's a need, BE FIRST!</div>
      <div><b>Service</b>Life is not about you, BE ABOUT OTHERS!</div>
    </div>
    <p class="abs values-close">These three values guide everything we do</p>

    <h2 class="abs story-title h-head">Our Story</h2>
    <div class="abs story-copy">
      <p>Built on solving complex plumbing challenges. Trusted for every plumbing need. Since our founding, Conduit Renewal Partners has built a reputation for solving complex plumbing and sewer problems through quality workmanship, professionalism, and innovative solutions. As our customers' needs have grown, so has our commitment to serving them.</p>
      <p>What began as a leader in pipe restoration has expanded into full-service plumbing, allowing us to provide complete solutions under one roof, from everyday repairs to major plumbing rehabilitation projects. Our business philosophy is a simple three-step approach: First, we listen to your needs. Second, we identify the best solutions. Third, we deliver the highest quality end result.</p>
    </div>
    <div class="abs story-foot">
      <div class="web-spaced">WWW.KVTFLOW.EXAMPLE</div>
      <div class="tagline">Reliable Repairs | Honest Service | Lasting Solutions</div>
    </div>

    <h2 class="abs services-title h-head">Complete Plumbing Solutions</h2>

    <div class="svc svc-repairs">
      <h3><svg viewBox="0 0 17 17" fill="none" stroke="#0054AA" stroke-width="1.4"><path d="M3 2V7H8V14M8 10H13V15M12 3Q14 5 12 7"/></svg>Plumbing Repairs</h3>
      <p>Reliable solutions to keep your plumbing system running safely and efficiently.</p>
      <ul><li>Leak detection &amp; repair</li><li>Pipe burst repairs</li><li>Water line repairs</li><li>Whole-home repiping</li></ul>
    </div>

    <div class="svc svc-fixtures">
      <h3><svg viewBox="0 0 17 17" fill="none" stroke="#0054AA" stroke-width="1.6"><path d="M3 14 13 4M4 3 14 13"/><circle cx="13" cy="4" r="2"/><circle cx="4" cy="3" r="1.5"/></svg>Fixtures &amp; Installations</h3>
      <p>Professional installation, repair, and replacement of the fixtures you use every day.</p>
      <div class="cols">
        <ul><li>Faucets</li><li>Toilets</li><li>Sinks</li><li>Showers &amp; tubs</li></ul>
        <ul><li>Garbage<br>disposals</li><li>Hose bibs</li><li>Shut-off valves</li></ul>
      </div>
    </div>

    <div class="svc svc-heater">
      <h3><svg viewBox="0 0 17 17" fill="none" stroke="#0054AA" stroke-width="1.4"><rect x="4" y="3" width="9" height="12" rx="2"/><path d="M6 1V3M11 1V3M7 8Q8.5 6 8.5 9Q10 8 10 10Q10 12 8.5 12Q7 12 7 10"/></svg>Water Heater Services</h3>
      <p>Whether you need a repair, replacement, or routine maintenance, we'll keep your hot water flowing.</p>
      <ul><li>Water heater repair</li><li>Water heater replacement</li><li>Tankless water heaters</li><li>Expansion tanks</li><li>Recirculation pumps</li><li>Preventative maintenance</li></ul>
    </div>

    <div class="svc svc-drain">
      <h3><svg viewBox="0 0 17 17" fill="none" stroke="#0054AA" stroke-width="1.4"><path d="M2 10H15V12Q15 15 8.5 15Q2 15 2 12Z"/><path d="M8.5 3V8M6 5Q8.5 1 11 5"/></svg>Drain &amp; Sewer Solutions</h3>
      <p>From routine drain cleaning to complete sewer repairs, our team has the equipment and expertise to get your plumbing flowing again.</p>
      <ul><li>Drain cleaning</li><li>Hydro jetting</li><li>Camera inspections</li><li>Main sewer line cleaning</li><li>Sewer line repair</li><li>Sewer line replacement</li><li>Emergency drain backups</li></ul>
    </div>

    <div class="abs services-logo brand-mark"><span class="sq"></span><span class="name">KVT</span></div>
    <div class="abs services-logo-sub brand-sub">CONDUIT RENEWAL PARTNERS</div>

    <div class="photo heater-photo" role="img" aria-label="Photo of water heater pipe fittings and valves"></div>
    <div class="abs inner-foot">
      <div class="phone-big">800-318-4957</div>
      <div class="web-spaced">WWW.KVTFLOW.EXAMPLE</div>
      <div class="tagline">Reliable Repairs | Honest Service | Lasting Solutions</div>
    </div>
  </div>
</section>

</body>
</html>
```